Business Card Design

Copperfield Lantern Works, Inc. (CLW), located in Memphis, TN began operating on 2003. We are a certified
minority woman-owned business that genuinely takes a vested interest in our customers. We serve utilities,
government, contractors and end user markets in electrical, water, gas and industrial supplies. Our core
competency as a distributor of electrical materials has positioned us to serve business of all size. As your supply
chain partner, we arm you with the resources you need to make your supply chain more efficient. Our team
works with your team on a daily basis to help you solve problems and achieve goals. This team approach has
helped CLW customers to succeed and we can do the same for you.

NAICS Codes:
423610 Electrical Apparatus and Equipment, Wiring Supplies, and Related Equipment Merchant
Wholesalers
423510 Metal Service Centers and Other Metal Merchant Wholesalers
423720 Plumbing and Heating Equipment and Supplies (Hydronics) Merchant Wholesalers

Certifications
MBE (KRVPQAL, State of Tennessee Up-RFX and HJW), WBE (QOZRT),
WOSB, DOT (TDOT, MDOT, ALDOT, SCDOT, NCDOT, and VDOT), LOSB,
SBE, and LSB Certified
Some of Our Products Include:
. Boxes & Covers
. Conduit & Raceway
. Fittings
. Fuses
. Lamp & Ballasts
. Lighting Controls & Timers
. Lighting Fixtures
. Personal Safety
. Pipes
. Power Distribution
. Terminations Ground & Splices
. Tools & Testers
. Wire, Cords & Cable
. Wiring Devices
. Valves

Industry/Entity Type

Business

Contact Information for Business Card

Harriet M. Pendlow - President/CEO
4817 Galvin Ave., Memphis, TN 38127
901-482-6317 office, 901-482-6319 fax, 901-358-2074 cell
hmpendlow@clwgroupx.com - www.clwworksx.com

```html
<!DOCTYPE html>
<html lang="en">
<head>
<meta charset="utf-8">
<title>Copperfield Lantern Works – Business Card</title>
<link href="https://fonts.googleapis.com/css2?family=Open+Sans:wght@400;600&display=swap" rel="stylesheet">
<style>
  :root {
    --green: #9cae1c;
    --green-dark: #7f8f12;
    --ink: #2a2a2a;
    --paper: #ffffff;
    --backdrop: #e9e7e2;
  }
  * { margin: 0; padding: 0; box-sizing: border-box; }
  html, body { width: 1200px; height: 902px; overflow: hidden; }
  body {
    background: var(--backdrop);
    font-family: "Open Sans", Arial, sans-serif;
    color: var(--ink);
    position: relative;
  }
  .card {
    position: absolute;
    left: 250px;
    width: 700px;
    height: 400px;
    background: var(--paper);
    box-shadow: 0 4px 14px rgba(0,0,0,.18);
    overflow: hidden;
  }
  .card--back { top: 34px; }
  .card--front { top: 468px; }
  .card svg.shapes { position: absolute; inset: 0; width: 100%; height: 100%; }

  .brand { position: absolute; display: flex; align-items: flex-start; gap: 10px; }
  .brand__mark { width: 14px; height: 14px; background: var(--green); margin-top: 8px; }
  .brand__name { font-weight: 400; color: var(--ink); line-height: 1.05; letter-spacing: .5px; }
  .brand__name span { display: block; }

  /* back */
  .card--back .brand { left: 60px; top: 48px; }
  .card--back .brand__name { font-size: 26px; }
  .products__title { position: absolute; left: 360px; top: 62px; font-size: 19px; }
  .products { position: absolute; list-style: none; font-size: 18px; line-height: 27px; }
  .products li { display: flex; align-items: center; gap: 10px; }
  .products li::before { content: ""; width: 6px; height: 10px; background: var(--ink); border-radius: 2px; }
  .products--left { left: 70px; top: 130px; }
  .products--right { left: 400px; top: 130px; }

  /* front */
  .card--front .brand { left: 60px; top: 92px; }
  .card--front .brand__name { font-size: 34px; }
  .holder { position: absolute; left: 400px; top: 128px; width: 280px; text-align: right; }
  .holder__name { font-size: 25px; line-height: 1.1; }
  .holder__title { font-size: 16px; }
  .contact { position: absolute; right: 22px; top: 208px; list-style: none; font-size: 17px; line-height: 27px; text-align: right; }
  .contact li { display: flex; justify-content: flex-end; align-items: center; gap: 8px; }
  .phones { position: absolute; left: 46px; top: 228px; list-style: none; font-size: 20px; line-height: 30px; }
  .phones li { display: flex; align-items: center; gap: 10px; }
  .icon { width: 20px; height: 20px; flex: none; }
  .icon--blank { visibility: hidden; }
</style>
</head>
<body>

<section class="card card--back" aria-label="Card back">
  <svg class="shapes" viewBox="0 0 700 400" aria-hidden="true">
    <rect x="0" y="352" width="700" height="22" fill="var(--green)"/>
  </svg>
  <div class="brand">
    <div class="brand__mark"></div>
    <div class="brand__name"><span>COPPERFIELD</span><span>LANTERN WORKS</span></div>
  </div>
  <h2 class="products__title" style="font-weight:400">Our Products Include</h2>
  <ul class="products products--left">
    <li>Boxes &amp; Covers</li>
    <li>Conduit &amp; Raceway</li>
    <li>Fittings</li>
    <li>Fuses</li>
    <li>Lamp &amp; Ballasts</li>
    <li>Lighting Controls &amp; Timers</li>
    <li>Lighting Fixtures</li>
    <li>Personal Safety</li>
  </ul>
  <ul class="products products--right">
    <li>Pipes</li>
    <li>Power Distribution</li>
    <li>Terminations Ground &amp; Splices</li>
    <li>Tools &amp; Testers</li>
    <li>Wire, Cords &amp; Cable</li>
    <li>Wiring Devices</li>
    <li>Valves</li>
  </ul>
</section>

<section class="card card--front" aria-label="Card front">
  <svg class="shapes" viewBox="0 0 700 400" aria-hidden="true">
    <polygon points="330,112 700,112 700,176 430,176" fill="var(--green)"/>
    <line x1="398" y1="250" x2="398" y2="330" stroke="var(--green)" stroke-width="3"/>
    <polygon points="0,346 372,310 372,400 0,400" fill="var(--green)"/>
  </svg>

  <div class="brand">
    <div class="brand__mark"></div>
    <div class="brand__name"><span>COPPERFIELD</span><span>LANTERN WORKS</span></div>
  </div>

  <div class="holder">
    <div class="holder__name">Harriet M. Pendlow</div>
    <div class="holder__title">President/CEO</div>
  </div>

  <ul class="contact">
    <li>hmpendlow@clwgroupx.com
      <svg class="icon" viewBox="0 0 20 20"><rect width="20" height="20" rx="5" fill="var(--green)"/><rect x="4" y="6" width="12" height="8" fill="none" stroke="#fff" stroke-width="1.5"/><polyline points="4,6 10,11 16,6" fill="none" stroke="#fff" stroke-width="1.5"/></svg></li>
    <li>www.clwworksx.com
      <svg class="icon" viewBox="0 0 20 20"><rect width="20" height="20" rx="5" fill="var(--green)"/><circle cx="10" cy="10" r="5.5" fill="none" stroke="#fff" stroke-width="1.5"/><line x1="4.5" y1="10" x2="15.5" y2="10" stroke="#fff" stroke-width="1.2"/><ellipse cx="10" cy="10" rx="2.3" ry="5.5" fill="none" stroke="#fff" stroke-width="1.2"/></svg></li>
    <li>4817 Galvin Ave.,
      <svg class="icon" viewBox="0 0 20 20"><rect width="20" height="20" rx="5" fill="var(--green)"/><path d="M10 16 L6 10 A4 4 0 1 1 14 10 Z" fill="#fff"/><circle cx="10" cy="8.5" r="1.5" fill="var(--green)"/></svg></li>
    <li>Memphis, TN 38127 <svg class="icon icon--blank" viewBox="0 0 20 20"></svg></li>
  </ul>

  <ul class="phones">
    <li><svg class="icon" viewBox="0 0 20 20"><rect width="20" height="20" rx="5" fill="var(--green)"/><path d="M5 8 Q10 4 15 8 L13 9 L12 7.5 Q10 7 8 7.5 L7 9 Z" fill="#fff"/><rect x="6" y="10" width="8" height="5" rx="1" fill="#fff"/></svg>901-482-6317</li>
    <li><svg class="icon" viewBox="0 0 20 20"><rect width="20" height="20" rx="5" fill="var(--green)"/><rect x="7" y="4" width="6" height="12" rx="1" fill="none" stroke="#fff" stroke-width="1.5"/><rect x="8.5" y="6" width="3" height="4" fill="#fff"/></svg>901-358-2074</li>
    <li><svg class="icon" viewBox="0 0 20 20"><rect width="20" height="20" rx="5" fill="var(--green)"/><rect x="5" y="8" width="10" height="7" rx="1" fill="#fff"/><rect x="7" y="4" width="6" height="4" fill="none" stroke="#fff" stroke-width="1.3"/></svg>901-482-6319</li>
  </ul>
</section>

</body>
</html>
```